Business card design and logo needed - Photographer

I take photos of weddings, rodeos, snowmobiling.
Need a card to hand out to prospective clients.
Industry/Entity Type
Business
Contact Information for Business Card
Marcus Dolven Photography
Requirements
Must have
- Bold
Black or white base.
My website. www.MarcusDolven.example
Should not have
- camera/ lens/ aperture blades

```html
<!DOCTYPE html>
<html lang="en">
<head>
<meta charset="UTF-8">
<title>Marcus Dolven Photography – Business Card</title>
<link rel="stylesheet" href="https://fonts.googleapis.com/css2?family=Quicksand:wght@400&display=swap">
<style>
  :root {
    --card-white: #ffffff;
    --block-charcoal: #272727;
    --text-light: #f4f4f4;
    --text-dark: #2b2b2b;
    --rule-grey: #8a8a8a;
  }
  * { margin: 0; padding: 0; box-sizing: border-box; }
  html, body {
    width: 694px;
    height: 1200px;
    overflow: hidden;
    background: var(--card-white);
  }
  .card {
    position: relative;
    width: 694px;
    height: 1200px;
    background: var(--card-white);
    font-family: "Quicksand", sans-serif;
  }
  .brand-block {
    position: absolute;
    left: 46px;
    top: 0;
    width: 602px;
    height: 705px;
    background: var(--block-charcoal);
  }
  .brand-name {
    position: absolute;
    right: 36px;
    bottom: 46px;
    font-size: 46px;
    font-weight: 400;
    line-height: 1.2;
    text-align: right;
    color: var(--text-light);
  }
  .brand-name span { display: block; }
  .divider {
    position: absolute;
    left: 46px;
    top: 996px;
    width: 602px;
    border-top: 2px dotted var(--rule-grey);
  }
  .contact {
    position: absolute;
    left: 46px;
    top: 1028px;
    list-style: none;
    color: var(--text-dark);
    font-weight: 400;
  }
  .contact li {
    font-size: 28px;
    line-height: 47px;
  }
  .contact .phone { font-size: 31px; }
</style>
</head>
<body>
  <div class="card">
    <div class="brand-block">
      <h1 class="brand-name"><span>Marcus Dolven</span><span>Photography</span></h1>
    </div>
    <div class="divider"></div>
    <ul class="contact">
      <li class="phone">(555) 014 2273</li>
      <li class="website">www.marcusdolven.example</li>
      <li class="social">www.social.example/marcus.dolven</li>
    </ul>
  </div>
</body>
</html>
```